Scientific Conference A0 Poster

I need an A0 poster for a Emergency Medicine scientific conference designed urgently. Attached is the information needed/specification,
as well as a previous poster. Your creativity is much appreciated. Here is a link to how to create a poster (no doubt things you already know), there are also examples of other posters medical posters. I want mine to be the best.
https://www.vexlorstudy.co.uk/bripmed/how-to-make-a-poster/
Please keep the Holbury and Penwick Care Trust and PCS logos/graphics
Please can you find a way to graphically represent the visual elements listed in the specification as well as the statistics listed in the specification. The statistics should not just be quoted, they need to be graphically represented, if possible. I am comfortable with whatever you think works.
Doctors and Healthcare management
Healthcare

```html
<!DOCTYPE html>
<html lang="en">
<head>
<meta charset="utf-8">
<title>Crowding in Emergency Departments During COVID-19 – Conference Poster</title>
<link href="https://fonts.googleapis.com/css2?family=Poppins:wght@400;500;600;700;800&display=swap" rel="stylesheet">
<style>
  :root{
    --primary-blue:#005eb8;
    --accent-blue:#1f7bf0;
    --navy:#0b1f44;
    --deep-navy:#041d45;
    --cyan:#36c3e6;
    --sky:#2a9fe0;
    --orange:#e8590c;
    --pale:#eaf2fc;
    --pale-2:#d9e8fa;
    --ink:#111a2b;
    --white:#ffffff;
  }
  *{box-sizing:border-box;margin:0;padding:0}
  html,body{width:904px;height:1200px;overflow:hidden;background:#fff}
  body{font-family:"Poppins",sans-serif;color:var(--ink)}
  .abs{position:absolute}
  .poster{position:relative;width:904px;height:1200px;overflow:hidden;background:var(--white)}

  /* header */
  .brand{left:38px;top:34px;width:230px;height:90px;color:var(--primary-blue);font-weight:800;font-size:70px;line-height:90px;text-align:center;letter-spacing:3px}
  .title{left:350px;top:33px;color:#fff;font-weight:800;text-transform:uppercase;font-size:30px;line-height:29px;white-space:nowrap}
  .title .line-1{color:var(--navy);letter-spacing:4.2px}
  .subtitle{left:352px;top:102px;color:#fff;font-size:12.6px;line-height:16px;width:420px}
  .doctor{left:421px;top:152px;color:var(--accent-blue);font-weight:800;font-size:25px;line-height:44px;white-space:nowrap}
  .divider{left:636px;top:163px;width:1.5px;height:22px;background:var(--accent-blue)}
  .role{left:648px;top:161px;color:#fff;font-size:10.5px;line-height:13px;letter-spacing:2.4px;font-weight:500}

  /* left column */
  .section-title{font-weight:700;font-size:14.5px;color:var(--ink);white-space:nowrap}
  .intro-title{left:37px;top:154px}
  .photo{left:37px;top:180px;width:296px;height:159px;background:linear-gradient(160deg,#cfd8e2 0%,#9fb0c2 45%,#6f8298 100%)}
  .caption{left:37px;top:341px;width:296px;height:35px;background:var(--primary-blue);color:#fff;font-weight:600;font-size:8.6px;line-height:11px;text-align:center;padding-top:7px}
  .body-text{font-size:8.8px;line-height:10.4px;color:var(--ink)}
  .intro-text{left:40px;top:382px;width:290px}
  .kicker{font-weight:700;font-size:8.2px;letter-spacing:1.8px;color:var(--primary-blue)}
  .intro-kicker{left:40px;top:419px}
  .intro-stat{left:40px;top:431px;width:290px}
  .chart-box{left:37px;top:477px;width:296px;height:197px;background:#f4f8fd;border:1px solid #9cc0e8}
  .source-label{font-size:8.4px;color:var(--ink)}
  .source-link{font-size:8.2px;font-weight:700;color:var(--primary-blue);line-height:10.5px}

  /* impact panel */
  .impact{left:38px;top:771px;width:307px;height:429px;background:var(--deep-navy)}
  .impact-title{left:54px;top:786px;color:var(--orange);font-weight:700;font-size:17px;line-height:20px}
  .impact-text{left:95px;width:240px;color:#fff;font-size:8.8px;line-height:10.4px}
  .impact-kicker{left:95px;top:943px;color:#2a8cf0;font-weight:700;font-size:9.5px;letter-spacing:2px}
  .impact-stat{left:100px;top:966px;width:70px;color:#fff;font-size:8.8px;line-height:13px}
  .mini-title{left:180px;top:966px;color:#fff;font-weight:700;font-size:6px}
  .mini-sub{left:180px;top:974px;color:#cfd8e6;font-size:4.4px;line-height:5.6px;width:110px}
  .impact-source{left:95px;top:1104px;color:#fff;font-size:8.8px}
  .impact-link{left:95px;top:1122px;width:240px;color:#2a8cf0;font-weight:700;font-size:8.2px;line-height:10.5px}

  /* right column */
  .right-pane{left:372px;top:184px;width:532px;height:232px;background:var(--pale)}
  .tech-pane{left:372px;top:416px;width:532px;height:206px;background:var(--pale-2)}
  .recs-pane{left:372px;top:622px;width:532px;height:233px;background:var(--deep-navy)}
  .refs-pane{left:372px;top:855px;width:532px;height:298px;background:var(--pale)}
  .addr-title{left:394px;top:199px}
  .tech-title{left:394px;top:436px}
  .node-title{font-weight:600;font-size:8px;line-height:9.2px;color:var(--sky)}
  .node-title.dark{color:var(--navy)}
  .node-text{font-size:6px;line-height:7.1px;color:#222}
  .card-title{font-weight:600;font-size:8px;line-height:9.2px;text-align:center}
  .card-text{font-size:5.8px;line-height:6.9px;text-align:center;color:#222}
  .recs-title{left:372px;top:643px;width:532px;text-align:center;color:var(--orange);font-weight:700;font-size:14.5px}
  .rec-title{font-weight:700;font-size:6.6px;line-height:7.6px;text-align:center;color:#fff}
  .rec-title.cyan{color:#38b6ff}
  .rec-text{font-size:5.1px;line-height:6px;text-align:center;color:#fff}
  .refs-title{left:400px;top:867px;font-weight:700;font-size:9px;letter-spacing:3px;color:var(--primary-blue)}
  .refs{left:400px;top:884px;width:478px;font-size:6.2px;line-height:7.6px;color:#1d2533}
  .refs p{margin-bottom:7.4px}
  .refs a{color:var(--primary-blue);font-weight:700;text-decoration:underline}
  .footer{left:344px;top:1153px;width:560px;height:47px;background:var(--primary-blue);color:#fff;font-weight:700;font-size:13px;line-height:47px;padding-left:12px;white-space:nowrap}
  svg{overflow:visible}
</style>
</head>
<body>
<main class="poster">

  <!-- header -->
  <svg class="abs" style="left:0;top:0" width="904" height="196" viewBox="0 0 904 196" aria-hidden="true">
    <polygon points="279,0 904,0 904,152 340,152" fill="var(--primary-blue)"/>
    <polygon points="0,8 277,8 282,16 0,16" fill="var(--navy)"/>
    <polygon points="0,0 279,0 277,8 0,8" fill="var(--primary-blue)"/>
  </svg>
  <div class="abs brand">PCS</div>
  <h1 class="abs title"><span class="line-1">Crowding in Emergency</span><br>Departments During COVID-19</h1>
  <p class="abs subtitle">A Critical Review of existing and novel measures adopted by global health institutions</p>

  <div class="abs right-pane"></div>
  <div class="abs tech-pane"></div>
  <div class="abs recs-pane"></div>
  <div class="abs refs-pane"></div>

  <svg class="abs" style="left:0;top:152px" width="904" height="44" viewBox="0 0 904 44" aria-hidden="true">
    <polygon points="374,0 904,0 904,44 392,44" fill="var(--deep-navy)"/>
  </svg>
  <div class="abs doctor">DR AMARA OKOLI</div>
  <div class="abs divider"></div>
  <div class="abs role">EMERGENCY MEDICINE<br>CONSULTANT</div>

  <!-- introduction -->
  <h2 class="abs section-title intro-title">Introduction and Background</h2>
  <div class="abs photo" role="img" aria-label="Photo of clinical staff in scrubs walking along a busy hospital corridor"></div>
  <p class="abs caption">Emergency departments (ED) experienced unprecedented crowding during the COVID-19 pandemic.</p>
  <p class="abs body-text intro-text">Hospitals faced increased healthcare demand, leading to overflows in intensive care units and emergency care, with limited hospital bed availability.</p>
  <p class="abs kicker intro-kicker">STATISTICAL DATA</p>
  <p class="abs body-text intro-stat">During COVID-19, daily admissions reached an average of 157 per day, with EDs spending 152 days in overcrowding. (Pevrault et al., 2021)</p>

  <div class="abs chart-box"></div>
  <svg class="abs" style="left:0;top:0" width="904" height="1200" viewBox="0 0 904 1200" aria-label="Line chart of hospital admissions in England">
    <text x="185" y="484" font-size="3.6" text-anchor="middle" fill="#444" letter-spacing=".4">HOSPITAL ADMISSIONS IN ENGLAND</text>
    <g stroke="#d4dbe4" stroke-width=".5">
      <line x1="77" y1="495" x2="305" y2="495"/><line x1="77" y1="519" x2="305" y2="519"/>
      <line x1="77" y1="543" x2="305" y2="543"/><line x1="77" y1="566" x2="305" y2="566"/>
      <line x1="77" y1="590" x2="305" y2="590"/><line x1="77" y1="614" x2="305" y2="614"/>
      <line x1="77" y1="638" x2="305" y2="638" stroke="#888"/>
    </g>
    <g font-size="3.6" fill="#555" text-anchor="end">
      <text x="74" y="496">30000</text><text x="74" y="520">25000</text><text x="74" y="544">20000</text>
      <text x="74" y="567">15000</text><text x="74" y="591">10000</text><text x="74" y="615">5000</text><text x="74" y="639">0</text>
    </g>
    <text x="56" y="566" font-size="3.4" fill="#555" transform="rotate(-90 56 566)" text-anchor="middle">NO. OF PATIENTS</text>
    <g font-size="3.2" fill="#555">
      <text transform="translate(84 660) rotate(-90)">01/04/2020</text>
      <text transform="translate(111 660) rotate(-90)">01/10/2020</text>
      <text transform="translate(138 660) rotate(-90)">01/04/2021</text>
      <text transform="translate(165 660) rotate(-90)">01/10/2021</text>
      <text transform="translate(192 660) rotate(-90)">01/04/2022</text>
      <text transform="translate(219 660) rotate(-90)">01/10/2022</text>
      <text transform="translate(246 660) rotate(-90)">01/04/2023</text>
      <text transform="translate(273 660) rotate(-90)">01/10/2023</text>
      <text transform="translate(300 660) rotate(-90)">01/04/2024</text>
    </g>
    <polyline fill="none" stroke="#9aa3ad" stroke-width=".8" points="84,636 110,636 124,632 130,630 138,635 160,636 200,635 240,636 262,636"/>
    <polyline fill="none" stroke="#1b5fc1" stroke-width="1.6" stroke-linejoin="round" points="80.6,547.4 84.1,580.8 89.1,614.2 98.4,635.6 105.5,636.6 116.2,614.2 124.7,566.5 129,511.7 132.5,542.7 137.5,599.9 144.6,628.5 151.8,633.2 158.9,621.3 166,623.7 173.1,614.2 180.2,618.9 183.8,609.4 187.4,566.5 191.6,599.9 194.5,595.1 200.2,568.9 205.2,609.4 210.1,616.5 214.4,585.6 219.4,618.9 224.4,604.6 230.1,595.1 234.4,621.3 238.6,607 244.3,599.9 250,618.9 255.7,609.4 262.1,604.6 269.2,623.7 276.4,634.7 283.5,628.5 290.6,618.9 295.6,628.5 301.3,623.7 304.8,626"/>
    <polyline fill="none" stroke="#f07a1a" stroke-width="1.6" stroke-dasharray="1 1.4" points="80.6,547.4 84.1,580.8 89.1,614.2 98.4,635.6 105.5,636.6 116.2,614.2 124.7,566.5 129,511.7 132.5,542.7 137.5,599.9 144.6,628.5 151.8,633.2 158.9,621.3 166,623.7 173.1,614.2 180.2,618.9 183.8,609.4 187.4,566.5 191.6,599.9 194.5,595.1 200.2,568.9 205.2,609.4 210.1,616.5 214.4,585.6 219.4,618.9 224.4,604.6 230.1,595.1 234.4,621.3 238.6,607 244.3,599.9 250,618.9 255.7,609.4 262.1,604.6"/>
  </svg>

  <p class="abs source-label" style="left:40px;top:681px">Global Figures Hub</p>
  <p class="abs source-link" style="left:40px;top:693px">https://globalfigureshub.org/grapher/uk-daily-covid-admissions</p>
  <p class="abs source-label" style="left:40px;top:713px">Bureau of National Figures</p>
  <p class="abs source-link" style="left:40px;top:725px;width:300px">https://www.natfigures.org.uk/peoplepopulationandcommunity/ healthandsocialcare/conditionsanddiseases/articles/ coronaviruscovid19latestinsights/hospitals</p>

  <!-- impact panel -->
  <div class="abs impact"></div>
  <h2 class="abs impact-title">The Impact of ED Crowding<br>During COVID-19</h2>
  <svg class="abs" style="left:0;top:0" width="904" height="1200" viewBox="0 0 904 1200" aria-hidden="true">
    <g fill="var(--primary-blue)">
      <polygon points="38,851 78,851 85,861 78,872 38,872 33,861"/>
      <polygon points="38,893 78,893 85,903 78,914 38,914 33,903"/>
      <polygon points="38,938 78,938 85,948 78,959 38,959 33,948"/>
    </g>
    <g fill="none" stroke="#fff" stroke-width=".9">
      <path d="M53,867 v-7 l6,-5 l6,5 v7 z M57,867 v-4 h4 v4"/>
      <path d="M58,896 l7,12 h-14 z M58,901 v4"/>
      <circle cx="64" cy="908" r="2.5"/>
      <path d="M52,953 h12 M54,953 v-3 M57,953 v-5 M60,953 v-4 M63,953 v-7 M53,946 l3,-2 l3,1 l4,-4"/>
    </g>
    <rect x="180" y="962" width="7" height="1.5" fill="#fff"/>
    <g stroke="#2b4a78" stroke-width=".4">
      <line x1="180" y1="988" x2="300" y2="988"/><line x1="180" y1="1000" x2="300" y2="1000"/>
      <line x1="180" y1="1011" x2="300" y2="1011"/><line x1="180" y1="1023" x2="300" y2="1023"/>
      <line x1="180" y1="1034" x2="300" y2="1034"/><line x1="180" y1="1057" x2="300" y2="1057"/>
    </g>
    <line x1="180" y1="1046" x2="300" y2="1046" stroke="#8ea3c2" stroke-width=".5"/>
    <g font-size="4" fill="#cfd8e6" text-anchor="end">
      <text x="315" y="989">10,000</text><text x="315" y="1001">8,000</text><text x="315" y="1012">6,000</text>
      <text x="315" y="1024">4,000</text><text x="315" y="1035">2,000</text><text x="315" y="1047">0</text><text x="315" y="1058">-2,000</text>
    </g>
    <polyline fill="none" stroke="#1e7be6" stroke-width="1.1" stroke-linejoin="round" points="181,1048 184,1042 187,1046 190,1040 193,1047 196,1043 199,1048 202,1041 205,1045 208,1038 211,1044 214,1046 217,1042 220,1047 223,1045 226,1047 229,1043 232,1046 235,1040 237,1034 239,991 241,1040 243,1046 246,1043 249,1039 251,1020 253,1042 256,1046 258,1035 261,1031 263,1038 266,1046 268,1042 271,1038 274,1035 277,1040 280,1033 283,1036 284,1030"/>
    <line x1="180" y1="1060" x2="300" y2="1060" stroke="#cfd8e6" stroke-width=".5"/>
    <g font-size="4.2" fill="#cfd8e6">
      <text x="182" y="1067">2016</text><text x="195" y="1067">17</text><text x="207" y="1067">18</text><text x="219" y="1067">19</text>
      <text x="231" y="1067">20</text><text x="243" y="1067">21</text><text x="255" y="1067">22</text>
    </g>
    <text x="180" y="1076" font-size="3.2" fill="#8ea3c2">Sources: BNF; The Ledger</text>
    <text x="300" y="1076" font-size="3.2" fill="#8ea3c2" text-anchor="end">*Four-week moving average</text>
  </svg>
  <p class="abs impact-text" style="top:847px">Overcrowding peaked during the pandemic, with a 28% increase following the removal of COVID-19 lockdowns. (Vorland et al., 2020)</p>
  <p class="abs impact-text" style="top:888px">This led to high-risk environments for both patients and staff, resulting in medical errors, prolonged hospital stays, and increased in-hospital mortality.</p>
  <p class="abs impact-kicker">STATISTICAL DATA</p>
  <p class="abs impact-stat">25% of patients required urgent hospital admission during the pandemic. (Casselo et al., 2020)</p>
  <p class="abs mini-title">Another bout of excess</p>
  <p class="abs mini-sub">England and Wales, number of deaths* compared with 2016-19 average</p>
  <p class="abs impact-source">The Ledger</p>
  <p class="abs impact-link">https://www.theledgerweekly.com/britain/2023/01/11/ how-many-excess-deaths-in-england-are-associated-with-a-and-e-delays</p>

  <!-- right column diagrams -->
  <svg class="abs" style="left:0;top:0" width="904" height="1200" viewBox="0 0 904 1200" aria-hidden="true">
    <defs>
      <filter id="soft" x="-40%" y="-40%" width="180%" height="180%"><feDropShadow dx="0" dy="2" stdDeviation="2" flood-color="#0b1f44" flood-opacity=".25"/></filter>
    </defs>
    <g fill="none" stroke-width="1">
      <path d="M518,247 H451 q-12,0 -12,12 V355" stroke="var(--cyan)"/>
      <path d="M459,380 H503" stroke="var(--cyan)"/>
      <path d="M568,247 H586" stroke="var(--sky)"/>
      <path d="M544,270 V367 q0,12 12,12 H628" stroke="var(--sky)"/>
      <path d="M678,380 H735" stroke="#1a3f8f"/>
      <path d="M735,247 H617 M735,247 H665 q-12,0 -12,12 V355" stroke="#1a3f8f"/>
      <path d="M785,247 H858 q12,0 12,12 V368 q0,12 -12,12 H773 q-12,0 -12,-12 V270" stroke="#1560d1"/>
    </g>
    <g filter="url(#soft)" fill="#fff">
      <circle cx="543" cy="244" r="25" stroke="var(--sky)" stroke-width="1.5"/>
      <circle cx="434" cy="380" r="25" stroke="var(--cyan)" stroke-width="1.5"/>
      <circle cx="653" cy="380" r="25" stroke="#1a3f8f" stroke-width="1.5"/>
      <circle cx="760" cy="245" r="25" stroke="#1560d1" stroke-width="1.5"/>
    </g>
    <g fill="none" stroke="var(--orange)" stroke-width="1">
      <circle cx="536" cy="238" r="4"/><rect x="540" y="245" width="12" height="6" rx="1.5"/><path d="M533,250 h6 M545,236 h8"/>
      <path d="M424,389 v-12 M424,384 h20 v5 M428,382 h6 v-3 h-6 z"/><circle cx="434" cy="371" r="4"/><path d="M434,369 v4 M432,371 h4"/>
      <rect x="644" y="374" width="10" height="10"/><circle cx="659" cy="382" r="3"/><path d="M648,372 l12,-6 l2,6"/>
      <path d="M750,256 h20 M753,256 v-6 M758,256 v-9 M763,256 v-7 M768,256 v-12 M751,244 l6,-4 l5,2 l7,-6"/>
    </g>
    <!-- tech cards -->
    <g fill="none" stroke-width="1">
      <rect x="394" y="491" width="107" height="119" rx="10" stroke="var(--cyan)"/>
      <rect x="516" y="491" width="107" height="119" rx="10" stroke="var(--sky)"/>
      <rect x="638" y="491" width="107" height="119" rx="10" stroke="#2b2f7e"/>
      <rect x="760" y="491" width="107" height="119" rx="10" stroke="#1560d1"/>
      <path d="M501,520 q8,0 8,8 v10 q0,8 8,8" stroke="var(--sky)"/>
      <path d="M623,540 q8,0 8,-8 v-4 q0,-8 8,-8" stroke="#2b2f7e"/>
      <path d="M745,525 q8,0 8,8 v24 q0,8 8,8" stroke="#1560d1"/>
    </g>
    <path d="M418,491 a31,31 0 0 1 62,0" fill="var(--cyan)"/>
    <path d="M538,491 a31,31 0 0 1 62,0" fill="var(--sky)"/>
    <path d="M660,491 a31,31 0 0 1 62,0" fill="#1b2a6b"/>
    <path d="M782,491 a31,31 0 0 1 62,0" fill="#1560d1"/>
    <g fill="#fff" filter="url(#soft)">
      <circle cx="449" cy="491" r="24"/><circle cx="569" cy="491" r="24"/><circle cx="691" cy="491" r="24"/><circle cx="813" cy="491" r="24"/>
    </g>
    <g fill="none" stroke="var(--orange)" stroke-width="1">
      <rect x="444" y="481" width="12" height="16" rx="2"/><path d="M450,485 v8 M446,489 h8 M438,497 l6,-8"/>
      <rect x="559" y="483" width="20" height="12" rx="2"/><path d="M563,487 h6 M563,491 h4 M572,489 h4"/>
      <circle cx="691" cy="491" r="8"/><ellipse cx="691" cy="491" rx="13" ry="5"/><ellipse cx="691" cy="491" rx="5" ry="13"/>
      <path d="M803,502 h20 M806,502 v-6 M811,502 v-9 M816,502 v-7 M821,502 v-12 M804,490 l6,-4 l5,2 l7,-6"/>
    </g>
    <text x="691" y="493" font-size="5" font-weight="700" fill="var(--orange)" text-anchor="middle" font-family="Poppins, sans-serif">AI</text>
    <!-- recommendations -->
    <g fill="none" stroke-width="1">
      <path d="M446,701 H416 q-14,0 -14,14 V792 q0,14 14,14 H500 q14,0 14,-14" stroke="#2a8cf0"/>
      <path d="M486,701 H517 q14,0 14,14 V760" stroke="#2a8cf0"/>
      <path d="M531,760 v14 q0,6 6,6 q6,0 6,-6 V748 q0,-8 8,-8 q7,0 7,8 V786" stroke="#fff"/>
      <path d="M566,785 V715 q0,-14 14,-14 H677 q14,0 14,14 V792 q0,14 -14,14 H647" stroke="#38b6ff"/>
      <path d="M607,806 H580 q-14,0 -14,-14" stroke="#38b6ff"/>
      <path d="M691,780 v-6 q0,-6 6,-6 q7,0 7,8 V790 q0,6 6,6 q8,0 8,-8 V715 q0,-14 14,-14 H769" stroke="#fff"/>
      <path d="M809,701 H839 q14,0 14,14 V792 q0,14 -14,14 H740 q-14,0 -14,-14" stroke="#2a8cf0"/>
    </g>
    <g fill="#fff" filter="url(#soft)">
      <circle cx="466" cy="699" r="22" stroke="#fcd3b8" stroke-width="1.5"/>
      <circle cx="627" cy="806" r="22" stroke="#2a8cf0" stroke-width="1.5"/>
      <circle cx="789" cy="699" r="22" stroke="#2a8cf0" stroke-width="1.5"/>
    </g>
    <g fill="none" stroke="var(--orange)" stroke-width="1">
      <rect x="454" y="688" width="20" height="16" rx="2"/><circle cx="469" cy="702" r="5"/><path d="M473,706 l4,4 M460,700 v-5 M463,700 v-7"/>
      <path d="M614,806 l6,-6 h6 l4,4 l6,-2 l5,5 M617,808 l6,6 M621,806 l7,7 M625,805 l6,6"/><circle cx="627" cy="796" r="4"/><path d="M625,796 l1.5,1.5 l3,-3"/>
      <rect x="781" y="686" width="16" height="8" rx="3"/><circle cx="789" cy="704" r="3"/><circle cx="780" cy="706" r="2.5"/><circle cx="798" cy="706" r="2.5"/><path d="M783,714 q6,-7 12,0 M775,713 q5,-4 9,-1 M794,712 q4,-3 9,1"/>
    </g>
  </svg>

  <h2 class="abs section-title addr-title">Addressing ED Crowding</h2>
  <div class="abs" style="left:445px;top:284px;width:80px">
    <p class="node-title">Hospital<br>Transformations</p>
    <p class="node-text" style="margin-top:4px">Adaptations such as creating dedicated COVID-19 treatment zones and expanding telehealth services.</p>
  </div>
  <div class="abs" style="left:555px;top:291px;width:76px">
    <p class="node-title">Proces<br>Optimisation</p>
    <p class="node-text" style="margin-top:4px">Fast-track pathways, improved triage, and discharge planning were implemented to improve patient flow.</p>
  </div>
  <div class="abs" style="left:664px;top:283px;width:86px">
    <p class="node-title dark">Leadership &amp;<br>Training</p>
    <p class="node-text" style="margin-top:3px">Enhanced adaptability through evidence-based training programs, ensuring efficient ED management during surges.</p>
  </div>
  <div class="abs" style="left:770px;top:283px;width:96px">
    <p class="node-title" style="color:var(--accent-blue)">Statistical Data</p>
    <p class="node-text" style="margin-top:2px;padding-left:7px;text-indent:-6px"><span style="color:#2a8cf0">●</span> Each hour of ambulance diversion is associated with $1,086 deducted from hospital revenue (Ashcombe et al., 2020).</p>
    <p class="node-text" style="margin-top:5px;padding-left:7px;text-indent:-6px"><span style="color:#2a8cf0">●</span> Reducing ambulance diversion could save hospitals around $9,000 annually (Ashcombe et al., 2020).</p>
  </div>

  <h2 class="abs section-title tech-title">Technological Solutions for Managing ED Crowding</h2>
  <div class="abs" style="left:398px;top:534px;width:99px">
    <p class="card-title" style="color:#2ab3e0">Telemedicine</p>
    <p class="card-text" style="margin-top:6px">Remote delivery of healthcare services using telecommunication technologies.</p>
  </div>
  <div class="abs" style="left:520px;top:534px;width:99px">
    <p class="card-title" style="color:var(--sky)">Internet<br>Hospitals</p>
    <p class="card-text" style="margin-top:4px">Implementation of multi-centre internet hospitals to reduce physical ED visits and crowding.</p>
  </div>
  <div class="abs" style="left:642px;top:534px;width:99px">
    <p class="card-title" style="color:#1b2a6b">AI<br>Advancements</p>
    <p class="card-text" style="margin-top:4px">AI-enabled tools like virtual waiting rooms and online symptom checkers streamlined patient management.</p>
  </div>
  <div class="abs" style="left:764px;top:534px;width:99px">
    <p class="card-title" style="color:#1560d1">Statistical<br>Data</p>
    <p class="card-text" style="margin-top:4px">By the end of 2021, experts expected 1 billion telehealth visits globally (Varrel et al., 2021)</p>
  </div>

  <h2 class="abs recs-title">Recommendations for Future Crowding Management</h2>
  <div class="abs" style="left:408px;top:732px;width:117px">
    <p class="rec-title">Data-driven Real-Time<br>Bottleneck removal</p>
    <p class="rec-text" style="margin-top:5px">Live dashboards pinpoint resource constraints (imaging, labs, beds) and patient acuity for dynamic resource allocation and on-the-fly interventions.</p>
  </div>
  <div class="abs" style="left:570px;top:710px;width:117px">
    <p class="rec-title cyan">Empowered<br>Interdepartmental<br>Collaboration</p>
    <p class="rec-text" style="margin-top:4px">Interdepartmental visibility and shared ownership of patient flow. Multidisciplinary patient flow teams. Inpatient units proactively prepare for admissions, optimising bed availability</p>
  </div>
  <div class="abs" style="left:732px;top:732px;width:117px">
    <p class="rec-title cyan">Proactive<br>Community Car</p>
    <p class="rec-text" style="margin-top:5px">Leveraging telehealth and community partnerships for remote monitoring, virtual urgent care, and preventative care to reduce ED demand.</p>
  </div>

  <!-- references -->
  <h2 class="abs refs-title">REFERENCES</h2>
  <div class="abs refs">
    <p>Brennick, B., Tolvane, N., Marsk, L., Eldrin, T., &amp; Quassel, M. J. (2020). Emergency department crowding and hospital transformation during COVID-19, a retrospective, descriptive study of a university hospital in Stockholm, Sweden. Nordic Journal of Trauma and Acute Care, 28(1), 1-10.</p>
    <p>Pevrault, J. B., Lanquist, J., Ormeval, M., Tessick, J., &amp; Dravel, F. (2021). Emergency Department and Overcrowding During COVID-19 Outbreak; a Letter to Editor. Annals of Acute Care Medicine, 9(1).</p>
    <p>Corvane, A. P., Pellis, K., Wendrow, I., Haskel, P., &amp; Tomlyn, E. (2021). The International Council for Acute Care report on emergency department crowding and access block: A brief summary. Acute Care Medicine Journal, 38(3), 245-246.</p>
    <p>Roskin, J. F., Ferrow, B. C., &amp; Alden, K. C. (2020). Factors Affecting Emergency Department Crowding. Acute Medicine Clinics, 38(3), 573-587.</p>
    <p>Varrel, M. Q., Quint, F. J., Oxley, N., Denmar, S. E., Soreth, S. W. Q., Pell, B. K. K., ... &amp; Wrenford, M. E. H. (2021). A descriptive analysis of the impact of COVID-19 on Emergency Department attendance and visit characteristics in Singapore.</p>
    <p>Casselo, F., Dravino, I., Tensetti, R., Orbani, L., Lumiro, N., &amp; Feravo, G. M. (2020). Italy and COVID-19: the changing patient flow in an orthopedic trauma center emergency department.</p>
    <p>Vorland, L., Corvane, A. P., Wendrow, I., Brask, S., Hollin, D., Merrit, C. A., ... &amp; Tomlyn, E. (2020). Early lessons from COVID-19 that may reduce future emergency department crowding. Acute Medicine Australasia, 32(6), 1077-1079.</p>
    <p>Global Figures Hub. (2023). Number of COVID-19 patients newly admitted to hospitals in a given week. Retrieved from <a>https://globalfigureshub.org/grapher/uk-daily-covid-admissions</a> (Access date 1/10/24)</p>
    <p><a>https://www.natfigures.org.uk/peoplepopulationandcommunity/healthan-socialcare/conditionsanddiseases/articles/coronaviruscovid19latestinsights/hospitals</a> (Access date 1/10/24)</p>
    <p>Ashcombe, T., Larrow, E., Quenby, B., Tavish, M., &amp; Orrin, A. (2020). Redesigning emergency department operations amidst a viral pandemic. The Journal of Acute Care Practice, 38(7), 1448-1453.</p>
  </div>

  <footer class="abs footer">Royal Society of Acute Care Medicine Annual Scientific Conference, 2024</footer>
</main>
</body>
</html>
```